Korvane Sky Works, LLC - Business Card

I currently have a drone business that specializes in aerial photography, thermal image inspections, deer recovery, search and rescue, custom agricultural applications. i will attach my current business card as well as some logos to incorporate for a new up to date business card
Updates

Designs look the same

Sick

Target Market(s)

farmers, hunters

Contact Information for Business Card

name address phone number (as existing card i attached)

Requirements
Must have
• im good with existing business card, but would like an agricultural twist

```html
<!DOCTYPE html>
<html lang="en">
<head>
<meta charset="utf-8">
<title>Korvane Sky Works, LLC – Business Card</title>
<link href="https://fonts.googleapis.com/css2?family=Montserrat:wght@600;800&family=Open+Sans:wght@400;600&display=swap" rel="stylesheet">
<style>
  :root{
    --bg:#000000;
    --card:#ffffff;
    --green:#3f9a2b;
    --green-dark:#1f6b1a;
    --ink:#111111;
    --muted:#333333;
  }
  *{margin:0;padding:0;box-sizing:border-box}
  html,body{width:1200px;height:1197px;overflow:hidden;background:var(--bg)}
  .stage{position:relative;width:1200px;height:1197px;background:var(--bg)}
  .card{position:absolute;left:244px;width:709px;height:405px;background:var(--card);overflow:hidden}
  .card--front{top:126px}
  .card--back{top:666px}

  .brand{position:absolute;display:flex;flex-direction:column;align-items:center;
    font-family:"Montserrat",sans-serif;font-weight:800;color:var(--green);letter-spacing:2px}
  .brand__dot{border:6px solid var(--green);border-radius:50%}
  .brand--front{left:0;right:0;top:52px}
  .brand--front .brand__dot{width:170px;height:170px}
  .brand--front .brand__name{font-size:40px;margin-top:14px}
  .brand--back{left:90px;width:160px;top:62px}
  .brand--back .brand__dot{width:66px;height:66px;border-width:3px}
  .brand--back .brand__name{font-size:17px;margin-top:6px}

  .services{position:absolute;left:88px;top:224px;list-style:none;
    font-family:"Open Sans",sans-serif;font-size:13.5px;color:var(--ink)}
  .services li{position:relative;padding-left:10px;height:26px;line-height:20px}
  .services li::before{content:"";position:absolute;left:0;top:3px;width:3px;height:14px;background:var(--green)}

  .accent-top{position:absolute;left:372px;top:0;width:34px;height:58px;background:var(--green)}
  .accent-top::after{content:"";position:absolute;left:12px;top:20px;width:8px;height:38px;background:var(--ink);transform:skewX(-12deg)}
  .bar{position:absolute;height:11px;background:var(--green)}
  .bar--left{left:0;top:385px;width:177px;clip-path:polygon(0 0,96% 0,100% 100%,0 100%)}
  .bar--right{right:0;top:385px;width:228px;clip-path:polygon(4% 0,100% 0,100% 100%,0 100%)}

  .person{position:absolute;left:456px;top:84px;font-family:"Montserrat",sans-serif}
  .person__name{font-size:23px;font-weight:800;color:var(--ink);letter-spacing:.5px}
  .person__role{font-family:"Open Sans",sans-serif;font-size:12px;color:var(--green);margin-top:2px}

  .contacts{position:absolute;left:408px;top:168px;list-style:none;font-family:"Open Sans",sans-serif;font-size:13px;color:var(--ink)}
  .contacts li{display:flex;align-items:center;gap:16px;height:44px}
  .contacts svg{width:30px;height:30px;flex:none}
  .contacts .address{line-height:17px}
</style>
</head>
<body>
<main class="stage">
  <section class="card card--front" aria-label="Business card front">
    <div class="brand brand--front">
      <span class="brand__dot"></span>
      <span class="brand__name">KORVANE</span>
    </div>
  </section>

  <section class="card card--back" aria-label="Business card back">
    <div class="brand brand--back">
      <span class="brand__dot"></span>
      <span class="brand__name">KORVANE</span>
    </div>
    <ul class="services">
      <li>Thermal Image Inspections</li>
      <li>Deer Recovery</li>
      <li>Search &amp; Rescue</li>
      <li>Real Estate Photography</li>
    </ul>

    <div class="accent-top"></div>

    <div class="person">
      <p class="person__name">DORIAN HASKELL</p>
      <p class="person__role">Owner</p>
    </div>

    <ul class="contacts">
      <li>
        <svg viewBox="0 0 30 30"><circle cx="15" cy="15" r="15" fill="#111"/><path d="M10 9h3l1 4-2 1a8 8 0 0 0 4 4l1-2 4 1v3a2 2 0 0 1-2 2A11 11 0 0 1 8 11a2 2 0 0 1 2-2z" fill="#fff"/></svg>
        <span>555-204-6619</span>
      </li>
      <li>
        <svg viewBox="0 0 30 30"><circle cx="15" cy="15" r="15" fill="#111"/><circle cx="15" cy="15" r="7" fill="none" stroke="#fff" stroke-width="1.6"/><path d="M8 15h14M15 8c-3 4-3 10 0 14M15 8c3 4 3 10 0 14" fill="none" stroke="#fff" stroke-width="1.4"/></svg>
        <span>www.korvanesky.com</span>
      </li>
      <li>
        <svg viewBox="0 0 30 30"><circle cx="15" cy="15" r="15" fill="#111"/><rect x="8" y="10" width="14" height="10" fill="none" stroke="#fff" stroke-width="1.6"/><path d="M8 10l7 6 7-6" fill="none" stroke="#fff" stroke-width="1.6"/></svg>
        <span>korvanesky@mailbox.com</span>
      </li>
      <li>
        <svg viewBox="0 0 30 30"><circle cx="15" cy="15" r="15" fill="#111"/><path d="M15 7a5.5 5.5 0 0 0-5.5 5.5C9.5 17 15 23 15 23s5.5-6 5.5-10.5A5.5 5.5 0 0 0 15 7z" fill="#fff"/><circle cx="15" cy="12.5" r="2" fill="#111"/></svg>
        <span class="address">street, City, Country<br>State, 00</span>
      </li>
    </ul>

    <div class="bar bar--left"></div>
    <div class="bar bar--right"></div>
  </section>
</main>
</body>
</html>
```